Hello,
Corinne Haskett Equestrian needs a business card. We are a high performance show jumping stables based at Willowmere Reserve in morningotn. We pride ourselves on producing high quality show jumping horses and competing our stock at a high level. My business card need to have my logo on it, and i would like it to have a classic design with a modern touch. I would like it to have quite a natural feel about it. It needs to be in a font which is easy to read as I spend a lot of time competing internationally and overseas, and i need to be able to give it out to breeders and contacts where English isnt their first language. I will need it to include the following details:
-Corinne Haskett Equestrian
-Based at Willowmere Reserve Mornington
-Address: 17 Tremont Lane Mornington Victoria 3931
-Mobile number: 0412605948
- website: www.corinnehaskettequestrian.example
Target Market(s)
For business adults who english may not be their first language
Industry/Entity Type
Business

```html
<!DOCTYPE html>
<html lang="en">
<head>
<meta charset="utf-8">
<title>Corinne Haskett Equestrian — Business Card</title>
<link rel="stylesheet" href="https://fonts.googleapis.com/css2?family=Cinzel:wght@400&family=Arimo:wght@400;700&family=Questrial&display=swap">
<style>
  :root {
    --backdrop: #8d8d8f;
    --card: #f6f6f4;
    --ink: #2d2a26;
    --copper: #b8621b;
    --copper-text: #c9772e;
  }
  * { box-sizing: border-box; margin: 0; padding: 0; }
  html, body { width: 1200px; height: 900px; overflow: hidden; }
  body {
    background: var(--backdrop);
    display: flex;
    flex-direction: column;
    align-items: center;
    justify-content: center;
    gap: 60px;
  }
  .card {
    position: relative;
    width: 560px;
    height: 340px;
    background: var(--card);
    overflow: hidden;
    box-shadow: 0 6px 18px rgba(0,0,0,.25);
  }

  /* Front */
  .front-mark {
    position: absolute;
    left: 0; right: 0;
    top: 112px;
    display: flex;
    align-items: center;
    justify-content: center;
    gap: 14px;
  }
  .front-mark .dot {
    width: 26px; height: 26px;
    border-radius: 50%;
    background: var(--copper);
  }
  .brand-name {
    font-family: "Cinzel", serif;
    font-weight: 400;
    color: var(--ink);
    font-size: 27px;
    letter-spacing: 0.5px;
  }
  .front-stripes {
    position: absolute;
    left: 0; right: 0;
    bottom: 26px;
  }
  .front-stripes .rule { height: 5px; background: var(--ink); }
  .front-stripes .band { height: 7px; background: var(--copper); margin: 4px 0; }

  /* Back */
  .back-header { position: absolute; left: 0; top: 0; }
  .business-title {
    position: absolute;
    right: 26px;
    top: 88px;
    text-align: right;
    font-family: "Arimo", sans-serif;
    color: var(--ink);
  }
  .business-title .name { font-size: 21px; font-weight: 400; line-height: 1.1; }
  .business-title .base { font-size: 12px; font-weight: 400; letter-spacing: .2px; }
  .contacts {
    position: absolute;
    left: 26px;
    top: 160px;
    list-style: none;
    font-family: "Questrial", sans-serif;
    font-size: 13px;
    color: var(--copper-text);
  }
  .contacts li {
    display: flex;
    align-items: center;
    gap: 12px;
    height: 34px;
  }
  .contacts svg { width: 18px; height: 18px; flex: none; }
  .logo-panel {
    position: absolute;
    right: 0;
    top: 166px;
    width: 205px;
    height: 150px;
    background: var(--ink);
    border-radius: 28px 0 0 28px;
    display: flex;
    align-items: center;
    justify-content: center;
    text-align: center;
    padding: 0 14px;
  }
  .logo-panel .brand-name {
    color: var(--copper);
    font-size: 20px;
    line-height: 1.35;
  }
</style>
</head>
<body>

  <section class="card card-front" aria-label="Business card front">
    <div class="front-mark">
      <span class="dot" aria-hidden="true"></span>
      <span class="brand-name">Corinne Haskett Equestrian</span>
    </div>
    <div class="front-stripes" aria-hidden="true">
      <div class="rule"></div>
      <div class="band"></div>
      <div class="rule"></div>
    </div>
  </section>

  <section class="card card-back" aria-label="Business card back">
    <svg class="back-header" width="560" height="90" viewBox="0 0 560 90" aria-hidden="true">
      <polygon points="0,0 560,0 560,48 400,48 360,60 0,60" fill="var(--copper)"/>
      <polyline points="0,62 360,62 400,50 560,50" fill="none" stroke="var(--ink)" stroke-width="4"/>
      <polygon points="400,53 560,53 560,90 540,90" fill="var(--card)"/>
      <polyline points="402,52 560,76" fill="none" stroke="var(--ink)" stroke-width="0"/>
    </svg>

    <div class="business-title">
      <p class="name">Corinne Haskett Equestrian</p>
      <p class="base">Based at Willowmere Reserve Mornington</p>
    </div>

    <ul class="contacts">
      <li>
        <svg viewBox="0 0 20 20" aria-hidden="true"><g fill="none" stroke="var(--ink)" stroke-width="1.4"><circle cx="10" cy="10" r="8"/><ellipse cx="10" cy="10" rx="3.5" ry="8"/><line x1="2" y1="10" x2="18" y2="10"/><line x1="3.5" y1="6" x2="16.5" y2="6"/><line x1="3.5" y1="14" x2="16.5" y2="14"/></g></svg>
        <span>www.corinnehaskettequestrian.example</span>
      </li>
      <li>
        <svg viewBox="0 0 20 20" aria-hidden="true"><path d="M10 1.5a6 6 0 0 0-6 6c0 4.5 6 11 6 11s6-6.5 6-11a6 6 0 0 0-6-6z" fill="var(--ink)"/><circle cx="10" cy="7.5" r="2.2" fill="var(--card)"/></svg>
        <span>17 Tremont Lane Mornington Victoria 3931</span>
      </li>
      <li>
        <svg viewBox="0 0 20 20" aria-hidden="true"><rect x="5" y="1.5" width="10" height="17" rx="2" fill="none" stroke="var(--ink)" stroke-width="1.4"/><line x1="8.5" y1="15.5" x2="11.5" y2="15.5" stroke="var(--ink)" stroke-width="1.4"/></svg>
        <span>0412605948</span>
      </li>
    </ul>

    <div class="logo-panel">
      <span class="brand-name">Corinne Haskett Equestrian</span>
    </div>
  </section>

</body>
</html>
```